New Law Firm needs a business card design

I need a business card for my new law firm called Tansey Wills and Probate. I would like designs to use my logo attached. My firm is new and modern. I like the colors orange, white, grey and black. The design I will chose will be one which uses color well, one which looks impressive, smart and modern.

Target Market(s)

Adults aged 30 to 50 seeking professional advice.

Industry/Entity Type

Law Firm

Requirements
Must have
• My logo which is attached.

Must have a modern font, similar to my logo and draft business card.
Should not have
• Any symbols about law, such as scales etc.

```html
<!DOCTYPE html>
<html lang="en">
<head>
<meta charset="utf-8">
<title>Tansey Wills and Probate – Business Card</title>
<link rel="stylesheet" href="https://fonts.googleapis.com/css2?family=Lato:wght@300;400;700&display=swap">
<style>
  :root {
    --stage: #3a3a3a;
    --card-white: #ffffff;
    --slate: #616161;
    --orange: #f28a1c;
    --ink: #111111;
    --text-grey: #555555;
    --logo-grey: #6f6f6f;
  }
  * { margin: 0; padding: 0; box-sizing: border-box; }
  html, body {
    width: 1200px; height: 926px; overflow: hidden;
    background: var(--stage);
    font-family: "Lato", sans-serif;
  }
  .canvas {
    position: relative; width: 1200px; height: 926px;
    display: flex; flex-direction: column; align-items: center; justify-content: center; gap: 46px;
  }
  .card {
    position: relative; width: 600px; height: 343px;
    background: var(--card-white); overflow: hidden;
    box-shadow: 0 8px 24px rgba(0,0,0,.35);
  }
  .card-shapes { position: absolute; inset: 0; width: 100%; height: 100%; }
  .shape-slate { fill: var(--slate); }
  .shape-orange { fill: var(--orange); }

  .brand { position: absolute; display: flex; align-items: center; gap: 10px; }
  .brand-dot { width: 14px; height: 14px; border-radius: 50%; background: var(--orange); flex: none; }
  .brand-name {
    font-weight: 400; font-size: 19px; letter-spacing: 1.5px;
    color: var(--logo-grey); text-transform: uppercase; line-height: 1.2;
  }

  .front .brand { left: 44px; top: 62px; }
  .holder { position: absolute; left: 44px; top: 190px; white-space: nowrap; }
  .holder-name { font-size: 30px; font-weight: 400; color: var(--ink); letter-spacing: -.3px; }
  .holder-name strong { font-weight: 700; }
  .holder-role { font-size: 17px; color: var(--orange); font-weight: 400; letter-spacing: .5px; }
  .holder-quals { margin-top: 8px; font-size: 15px; color: var(--text-grey); }

  .back .brand { left: 40px; top: 70px; }
  .contact { position: absolute; right: 34px; color: #fff; text-align: right; font-weight: 400; }
  .contact-address { top: 40px; display: flex; gap: 10px; align-items: flex-start; font-size: 14px; line-height: 1.35; }
  .contact-list { bottom: 40px; list-style: none; font-size: 14.5px; }
  .contact-list li { display: flex; justify-content: flex-end; align-items: center; gap: 10px; margin-top: 6px; }
  .icon-box {
    width: 20px; height: 20px; background: var(--orange);
    display: flex; align-items: center; justify-content: center; flex: none;
  }
  .icon-box svg, .pin svg { display: block; }
</style>
</head>
<body>
<main class="canvas">

  <section class="card front" aria-label="Business card front">
    <svg class="card-shapes" viewBox="0 0 600 343" preserveAspectRatio="none" aria-hidden="true">
      <path class="shape-orange" d="M452 0 L482 0 C474 120 428 250 366 343 L346 343 C406 250 448 120 452 0 Z"/>
      <path class="shape-slate" d="M492 0 L600 0 L600 343 L378 343 C440 250 484 120 492 0 Z"/>
    </svg>
    <div class="brand">
      <span class="brand-dot"></span>
      <span class="brand-name">Tansey Wills and Probate</span>
    </div>
    <div class="holder">
      <p class="holder-name">Daniel <strong>Carver</strong> <span class="holder-role">- LAWYER</span></p>
      <p class="holder-quals">Assoc.Deg.Law, BLJSt, LLB, Grad Dip Law.</p>
    </div>
  </section>

  <section class="card back" aria-label="Business card back">
    <svg class="card-shapes" viewBox="0 0 600 343" preserveAspectRatio="none" aria-hidden="true">
      <path class="shape-orange" d="M250 0 L292 0 C262 140 172 268 84 343 L60 343 C160 260 235 140 250 0 Z"/>
      <path class="shape-slate" d="M302 0 L600 0 L600 343 L96 343 C184 268 272 140 302 0 Z"/>
    </svg>
    <div class="brand">
      <span class="brand-dot"></span>
      <span class="brand-name">Tansey Wills<br>and Probate</span>
    </div>
    <div class="contact contact-address">
      <p>14 Harbour Lane,<br>Suite #210, Kent Bldg, NY 82417</p>
      <span class="pin">
        <svg width="18" height="24" viewBox="0 0 18 24" aria-hidden="true">
          <path d="M9 0C4 0 0 4 0 9c0 6.5 9 15 9 15s9-8.5 9-15C18 4 14 0 9 0Z" fill="#9a9a9a"/>
          <circle cx="9" cy="9" r="3.5" fill="#616161"/>
        </svg>
      </span>
    </div>
    <ul class="contact contact-list">
      <li>555 014 2290
        <span class="icon-box"><svg width="12" height="12" viewBox="0 0 12 12" aria-hidden="true"><path d="M2.5 0.5l2 2.5-1.2 1.3c.7 1.6 2 2.9 3.4 3.4L8 6.5l2.5 2-1 2.5C5 11 1 7 1 1.5Z" fill="#fff"/></svg></span>
      </li>
      <li>555 018 7734
        <span class="icon-box"><svg width="12" height="12" viewBox="0 0 12 12" aria-hidden="true"><rect x="3" y="0.5" width="6" height="3" fill="#fff"/><rect x="0.5" y="4" width="11" height="5" rx="1" fill="#fff"/><rect x="3" y="8" width="6" height="3.5" fill="#fff" stroke="#f28a1c" stroke-width=".8"/></svg></span>
      </li>
      <li>daniel@tanseyprobate.com.au
        <span class="icon-box"><svg width="12" height="12" viewBox="0 0 12 12" aria-hidden="true"><rect x="0.8" y="1" width="10.4" height="7" fill="none" stroke="#fff" stroke-width="1.4"/><rect x="4" y="9" width="4" height="1.2" fill="#fff"/><rect x="2.5" y="10.2" width="7" height="1.2" fill="#fff"/></svg></span>
      </li>
    </ul>
  </section>

</main>
</body>
</html>
```